Corvane Building Materials letterhead template

Simple but professional letterhead template for business communication.
LOGO/name in upper left, balanced by company contact info on right upper.
Subject description, date...
addressee, cc: and BC: if applicable editable info..

Need extra days to review

```html
<!DOCTYPE html>
<html lang="en">
<head>
<meta charset="utf-8">
<title>Corvane Building Materials – Stationery</title>
<link href="https://fonts.googleapis.com/css2?family=Rubik:wght@700&family=Roboto:wght@400;500&display=swap" rel="stylesheet">
<style>
:root{
  --brand:#0759c2;
  --brand-dark:#0a4aa0;
  --paper:#ffffff;
  --backdrop:#cbcbcb;
  --ink:#3a3a3a;
  --rule:#b9b9b9;
  --shade:#e6e6e8;
}
*{box-sizing:border-box;margin:0;padding:0}
html,body{width:954px;height:1200px;overflow:hidden;background:var(--backdrop)}
body{position:relative;font-family:"Roboto",Arial,sans-serif;color:var(--ink)}
.piece{position:absolute;background:var(--paper);box-shadow:2px 3px 5px rgba(0,0,0,.28);overflow:hidden}
.abs{position:absolute}

/* name block that stands where the brand mark sits */
.brand{position:absolute;display:flex;align-items:center;gap:4px}
.brand-square{background:var(--brand);border-radius:3px;flex:none}
.brand-name{font-family:"Rubik",Arial,sans-serif;font-weight:700;color:var(--brand);text-transform:uppercase;letter-spacing:.06em;line-height:1.12}
.brand.on-blue .brand-square{background:#fff}
.brand.on-blue .brand-name{color:#fff}
.wordmark{position:absolute;font-family:"Rubik",Arial,sans-serif;font-weight:700;color:#fff;text-transform:uppercase;letter-spacing:.07em;line-height:1.3}

/* business card */
.card-band{position:absolute;left:0;top:19px;width:141px;height:37px;background:var(--brand)}
.card-name{position:absolute;left:18px;top:26px;color:#fff;font-weight:500;font-size:10px;letter-spacing:.02em}
.card-role{position:absolute;left:18px;top:38px;color:#fff;font-size:8px}
.card-contact{position:absolute;left:18px;top:107px;font-size:8px;line-height:10px;color:#555}
.card-contact div{display:flex;align-items:center;gap:3px}
.icon{width:7px;height:7px;flex:none}
.card-address{position:absolute;right:15px;top:117px;font-size:8px;line-height:10px;text-align:right;color:#555}

/* letter */
.contact-small{position:absolute;font-size:3.6px;line-height:4.6px;color:#555}
.head-rule{position:absolute;height:.6px;background:var(--rule)}
.salutation{position:absolute;font-size:5px}
.letter-body{position:absolute;font-size:3.3px;line-height:4.6px;color:#555}
.letter-body p{margin-bottom:3.6px}
.closing{font-size:3px;margin-top:3px}
.signature{width:44px;height:7px;margin-top:3px;background:linear-gradient(90deg,#d9d9d9,#efefef);border-radius:2px}

/* notebook */
.ruled{position:absolute;height:.6px;background:#cfcfcf}
.field{position:absolute;font-size:5px;font-weight:500;color:var(--brand);display:flex;gap:2px;align-items:flex-end}
.field span{display:block;border-bottom:.6px solid #aaa;width:45px;height:5px}
</style>
</head>
<body>

<!-- Business card front -->
<section class="piece" style="left:32px;top:75px;width:269px;height:154px">
  <div class="card-band"></div>
  <div class="card-name">DARREN HOLT</div>
  <div class="card-role">Manager</div>
  <div class="brand" style="left:145px;top:18px">
    <div class="brand-square" style="width:38px;height:38px;border-radius:8px"></div>
    <div class="brand-name" style="font-size:9.6px">Corvane<br>Building<br>Materials</div>
  </div>
  <div class="card-contact">
    <div><svg class="icon" viewBox="0 0 10 10"><path d="M2 1h2l1 2.5-1.3 1a6 6 0 0 0 2.8 2.8l1-1.3L10 7v2a1 1 0 0 1-1 1A9 9 0 0 1 0 2a1 1 0 0 1 1-1z" fill="var(--brand)"/></svg>555-014-2200</div>
    <div><svg class="icon" viewBox="0 0 10 10"><rect x=".5" y="2" width="9" height="6.5" rx="1" fill="var(--brand)"/><path d="M1 2.5l4 3 4-3" stroke="#fff" stroke-width=".9" fill="none"/></svg>office@corvanebuild.com</div>
    <div><svg class="icon" viewBox="0 0 10 10"><circle cx="5" cy="5" r="4.5" fill="var(--brand)"/><path d="M.5 5h9M5 .5c-2 2.5-2 6.5 0 9M5 .5c2 2.5 2 6.5 0 9" stroke="#fff" stroke-width=".7" fill="none"/></svg>www.corvanebuild.com</div>
  </div>
  <div class="card-address">Your Address, City<br>State, Zip 0000</div>
</section>

<!-- Business card back -->
<section class="piece" style="left:32px;top:247px;width:269px;height:153px;background:var(--brand)">
  <div class="wordmark" style="left:54px;top:30px;font-size:22px;line-height:31px">Corvane<br>Building<br>Materials</div>
</section>

<!-- Letterhead -->
<section class="piece" style="left:318px;top:75px;width:232px;height:328px">
  <div class="brand" style="left:21px;top:16px">
    <div class="brand-square" style="width:24px;height:24px;border-radius:5px"></div>
    <div class="brand-name" style="font-size:6.4px">Corvane<br>Building<br>Materials</div>
  </div>
  <div class="contact-small" style="left:168px;top:15px">Your Address, City<br>State, Zip 0000<br>555-014-2200<br>office@corvanebuild.com<br>www.corvanebuild.com</div>
  <div class="head-rule" style="left:21px;top:43px;width:190px"></div>
  <div class="salutation" style="left:21px;top:100px">Dear Mr. Alder,</div>
  <div class="letter-body" style="left:21px;top:115px;width:190px">
    <p>Thank you for choosing Corvane for your recent order of timber, cement and roofing sheets. Delivery to your site is scheduled for next week, and our yard team will confirm the exact time one day before arrival. Please keep the access gate clear for the truck.</p>
    <p>Attached you will find the updated quote for the second phase, including insulation panels, drywall and fixings. Prices are held for thirty days from the date of this letter.</p>
    <p>Our trade desk can also arrange cut-to-size lumber and bulk pallets at a reduced rate. If your plans change, simply call us and we will adjust the order without any extra charge to your account.</p>
    <p>We appreciate your trust and look forward to supporting your project through to completion.</p>
    <div class="closing">Sincerely,</div>
    <div class="signature" role="img" aria-label="Handwritten signature"></div>
  </div>
</section>

<!-- Compliment slip -->
<section class="piece" style="left:568px;top:75px;width:355px;height:154px">
  <div class="abs" style="left:0;top:11px;width:245px;height:31px;background:var(--brand)"></div>
  <div class="abs" style="left:13px;top:19px;font-size:5px;line-height:6.4px;color:#fff">Your Address, City<br>State, Zip 0000</div>
  <div class="brand" style="left:248px;top:9px">
    <div class="brand-square" style="width:33px;height:33px;border-radius:7px"></div>
    <div class="brand-name" style="font-size:8.4px">Corvane<br>Building<br>Materials</div>
  </div>
</section>

<!-- Envelope -->
<section class="piece" style="left:568px;top:248px;width:355px;height:154px">
  <svg class="abs" style="left:0;top:0" width="355" height="43" viewBox="0 0 355 43">
    <path d="M0 0H355L348 28Q344 42 330 42H25Q11 42 8 28Z" fill="var(--brand)"/>
  </svg>
  <div class="brand on-blue" style="left:141px;top:8px">
    <div class="brand-square" style="width:26px;height:26px;border-radius:6px"></div>
    <div class="brand-name" style="font-size:7px">Corvane<br>Building<br>Materials</div>
  </div>
</section>

<!-- Folder outside -->
<section class="piece" style="left:32px;top:423px;width:434px;height:307px">
  <div class="abs" style="left:0;top:0;width:217px;height:307px;background:var(--brand)"></div>
  <div class="wordmark" style="left:38px;top:112px;font-size:20px;line-height:27px">Corvane<br>Building<br>Materials</div>
  <div class="abs" style="left:217px;top:0;width:217px;height:307px;background:linear-gradient(120deg,#ffffff 30%,#e7e7e9 60%,#ffffff 90%)"></div>
  <div class="abs" style="left:217px;top:13px;width:135px;height:22px;background:var(--brand)"></div>
  <div class="abs" style="left:227px;top:17px;font-size:3.4px;line-height:4.3px;color:#fff">555-014-2200<br>office@corvanebuild.com<br>www.corvanebuild.com</div>
  <div class="abs" style="left:272px;top:15px;width:.5px;height:17px;background:#fff"></div>
  <div class="abs" style="left:276px;top:17px;font-size:3.4px;line-height:4.3px;color:#fff">Your Address<br>City<br>State, Zip 0000</div>
  <div class="brand" style="left:356px;top:13px">
    <div class="brand-square" style="width:22px;height:22px;border-radius:5px"></div>
    <div class="brand-name" style="font-size:6.3px">Corvane<br>Building<br>Materials</div>
  </div>
  <div class="brand" style="left:257px;top:130px">
    <div class="brand-square" style="width:48px;height:46px;border-radius:10px"></div>
    <div class="brand-name" style="font-size:12.4px">Corvane<br>Building<br>Materials</div>
  </div>
</section>

<!-- Folder inside -->
<section class="piece" style="left:495px;top:423px;width:427px;height:307px;background:linear-gradient(90deg,#f4f4f4 0%,#e9e9eb 48%,#cfcfd3 50%,#e3e3e6 70%,#ececee 100%)">
  <div class="abs" style="left:224px;top:12px;width:194px;height:220px;background:linear-gradient(135deg,#ffffff 40%,#efeff1 100%)">
    <div class="brand" style="left:17px;top:14px">
      <div class="brand-square" style="width:20px;height:20px;border-radius:4px"></div>
      <div class="brand-name" style="font-size:5.4px">Corvane<br>Building<br>Materials</div>
    </div>
    <div class="contact-small" style="left:141px;top:13px;font-size:3px;line-height:3.8px">Your Address, City<br>State, Zip 0000<br>555-014-2200<br>office@corvanebuild.com<br>www.corvanebuild.com</div>
    <div class="head-rule" style="left:17px;top:36px;width:160px"></div>
    <div class="salutation" style="left:17px;top:85px;font-size:4.2px">Dear Mr. Alder,</div>
    <div class="letter-body" style="left:17px;top:97px;width:160px;font-size:2.9px;line-height:3.9px">
      <p style="margin-bottom:3px">Thank you for choosing Corvane for your recent order of timber, cement and roofing sheets. Delivery to your site is scheduled for next week, and our yard team will confirm the exact time one day before arrival. Please keep the access gate clear for the truck.</p>
      <p style="margin-bottom:3px">Attached you will find the updated quote for the second phase, including insulation panels, drywall and fixings. Prices are held for thirty days from the date of this letter.</p>
      <p style="margin-bottom:3px">Our trade desk can also arrange cut-to-size lumber and bulk pallets at a reduced rate. If your plans change, simply call us and we will adjust the order without any extra charge to your account.</p>
      <p style="margin-bottom:3px">We appreciate your trust and look forward to supporting your project through to completion.</p>
      <div class="closing" style="font-size:2.6px">Sincerely,</div>
    </div>
  </div>
  <svg class="abs" style="left:0;top:197px" width="427" height="110" viewBox="0 0 427 110">
    <path d="M0 0H190Q198 0 199 8L213 110H0Z" fill="var(--brand)"/>
    <path d="M427 0H236Q228 0 227 8L213 110H427Z" fill="var(--brand)"/>
  </svg>
</section>

<!-- Notebook cover -->
<section class="abs" style="left:57px;top:766px;width:263px;height:359px">
  <div class="piece" style="left:9px;top:0;width:254px;height:359px;background:var(--brand)">
    <div class="abs" style="left:31px;top:0;width:2px;height:359px;background:#1d2a3d"></div>
    <div class="wordmark" style="left:45px;top:134px;font-size:24px;line-height:32px">Corvane<br>Building<br>Materials</div>
  </div>
  <svg class="abs" style="left:0;top:0" width="30" height="359" viewBox="0 0 30 359">
    <g fill="none" stroke="#1b1b1b" stroke-width="2.2" stroke-linecap="round">
      <path d="M2 12h22a3 3 0 0 1 0 6H2M2 15h24"/>
      <path d="M2 33h22a3 3 0 0 1 0 6H2M2 36h24"/>
      <path d="M2 54h22a3 3 0 0 1 0 6H2M2 57h24"/>
      <path d="M2 75h22a3 3 0 0 1 0 6H2M2 78h24"/>
      <path d="M2 96h22a3 3 0 0 1 0 6H2M2 99h24"/>
      <path d="M2 117h22a3 3 0 0 1 0 6H2M2 120h24"/>
      <path d="M2 138h22a3 3 0 0 1 0 6H2M2 141h24"/>
      <path d="M2 159h22a3 3 0 0 1 0 6H2M2 162h24"/>
      <path d="M2 180h22a3 3 0 0 1 0 6H2M2 183h24"/>
      <path d="M2 201h22a3 3 0 0 1 0 6H2M2 204h24"/>
      <path d="M2 222h22a3 3 0 0 1 0 6H2M2 225h24"/>
      <path d="M2 243h22a3 3 0 0 1 0 6H2M2 246h24"/>
      <path d="M2 264h22a3 3 0 0 1 0 6H2M2 267h24"/>
      <path d="M2 285h22a3 3 0 0 1 0 6H2M2 288h24"/>
      <path d="M2 306h22a3 3 0 0 1 0 6H2M2 309h24"/>
      <path d="M2 327h22a3 3 0 0 1 0 6H2M2 330h24"/>
    </g>
  </svg>
</section>

<!-- Notebook open -->
<section class="piece" style="left:393px;top:769px;width:503px;height:356px">
  <div class="brand" style="left:25px;top:18px">
    <div class="brand-square" style="width:27px;height:27px;border-radius:6px"></div>
    <div class="brand-name" style="font-size:7.4px">Corvane<br>Building<br>Materials</div>
  </div>
  <div class="field" style="left:168px;top:18px">Date:<span></span></div>
  <div class="field" style="left:168px;top:31px">Time:<span></span></div>
  <div class="brand" style="left:277px;top:18px">
    <div class="brand-square" style="width:27px;height:27px;border-radius:6px"></div>
    <div class="brand-name" style="font-size:7.4px">Corvane<br>Building<br>Materials</div>
  </div>
  <div class="field" style="left:419px;top:18px">Date:<span></span></div>
  <div class="field" style="left:419px;top:31px">Time:<span></span></div>

  <svg class="abs" style="left:0;top:0" width="503" height="356" viewBox="0 0 503 356">
    <g stroke="#d0d0d0" stroke-width=".6">
      <path d="M25 64.5H227M25 79H227M25 93.5H227M25 108H227M25 122.5H227M25 137H227M25 151.5H227M25 166H227M25 180.5H227M25 195H227M25 209.5H227M25 224H227M25 238.5H227M25 253H227M25 267.5H227M25 282H227M25 296.5H227M25 311H227M25 325.5H227"/>
      <path d="M277 64.5H479M277 79H479M277 93.5H479M277 108H479M277 122.5H479M277 137H479M277 151.5H479M277 166H479M277 180.5H479M277 195H479M277 209.5H479M277 224H479M277 238.5H479M277 253H479M277 267.5H479M277 282H479M277 296.5H479M277 311H479M277 325.5H479"/>
    </g>
    <g fill="none" stroke="#1b1b1b" stroke-width="2.4" stroke-linecap="round">
      <path d="M240 20h24M242 17h20a4 3 0 0 1 0 6h-20a4 3 0 0 1 0-6"/>
      <path d="M240 40h24M242 37h20a4 3 0 0 1 0 6h-20a4 3 0 0 1 0-6"/>
      <path d="M240 59h24M242 56h20a4 3 0 0 1 0 6h-20a4 3 0 0 1 0-6"/>
      <path d="M240 79h24M242 76h20a4 3 0 0 1 0 6h-20a4 3 0 0 1 0-6"/>
      <path d="M240 99h24M242 96h20a4 3 0 0 1 0 6h-20a4 3 0 0 1 0-6"/>
      <path d="M240 119h24M242 116h20a4 3 0 0 1 0 6h-20a4 3 0 0 1 0-6"/>
      <path d="M240 138h24M242 135h20a4 3 0 0 1 0 6h-20a4 3 0 0 1 0-6"/>
      <path d="M240 158h24M242 155h20a4 3 0 0 1 0 6h-20a4 3 0 0 1 0-6"/>
      <path d="M240 178h24M242 175h20a4 3 0 0 1 0 6h-20a4 3 0 0 1 0-6"/>
      <path d="M240 197h24M242 194h20a4 3 0 0 1 0 6h-20a4 3 0 0 1 0-6"/>
      <path d="M240 217h24M242 214h20a4 3 0 0 1 0 6h-20a4 3 0 0 1 0-6"/>
      <path d="M240 237h24M242 234h20a4 3 0 0 1 0 6h-20a4 3 0 0 1 0-6"/>
      <path d="M240 256h24M242 253h20a4 3 0 0 1 0 6h-20a4 3 0 0 1 0-6"/>
      <path d="M240 276h24M242 273h20a4 3 0 0 1 0 6h-20a4 3 0 0 1 0-6"/>
      <path d="M240 296h24M242 293h20a4 3 0 0 1 0 6h-20a4 3 0 0 1 0-6"/>
      <path d="M240 315h24M242 312h20a4 3 0 0 1 0 6h-20a4 3 0 0 1 0-6"/>
      <path d="M240 335h24M242 332h20a4 3 0 0 1 0 6h-20a4 3 0 0 1 0-6"/>
    </g>
  </svg>
</section>

</body>
</html>
```